Google slides for an upcoming presentation

I would like to recreate the jpeg to better match our company branding & color, as well as better resolution-- which is found in the PPTX. The slide should read....
"What are the biggest differences between Web 2.0 to Web 3.0"

Industry/Entity Type

Web3

Other font styles liked:
• Manrope

```html
<!DOCTYPE html>
<html lang="en">
<head>
<meta charset="UTF-8">
<title>Web 2.0 to Web 3.0 – Title Slide Options</title>
<link rel="stylesheet" href="https://fonts.googleapis.com/css2?family=Manrope:wght@300;400;800&family=Montserrat:wght@400;800;900&display=swap">
<style>
  :root {
    --board: #333333;
    --ink: #3a3a44;
    --ink-soft: #4a4a55;
    --num-top: #7a6478;
    --num-bottom: #4c5168;
    --lilac: #e6d3f0;
    --pink: #f8d3e8;
    --periwinkle: #d6dcf6;
    --sky: #c9e6f8;
    --peach: #fde9dc;
    --web-violet: #a9b2ff;
    --web-purple: #c38df5;
    --web-pink: #f7a9d4;
    --web-blush: #f9c9d9;
    --ring-pink: #f59ae0;
    --ring-blue: #8fd8f4;
    --white: #ffffff;
  }
  * { box-sizing: border-box; margin: 0; padding: 0; }
  html, body {
    width: 1200px; height: 1200px; overflow: hidden;
    background: var(--board);
  }
  .board { position: relative; width: 1200px; height: 1200px; }

  .slide {
    position: absolute; left: 151px; width: 944px; height: 531px; overflow: hidden;
    background:
      radial-gradient(ellipse 260px 200px at 100% 80%, rgba(248,196,228,.9), transparent 70%),
      radial-gradient(ellipse 300px 160px at 95% 0%, var(--sky), transparent 70%),
      radial-gradient(ellipse 340px 140px at 50% 105%, var(--peach), transparent 70%),
      linear-gradient(115deg, var(--lilac) 0%, var(--pink) 35%, #ecd6f1 55%, var(--periwinkle) 80%, #dcecf8 100%);
  }
  .slide--thin { top: 50px; }
  .slide--bold { top: 619px; }

  .slide__title {
    position: absolute; top: 28px; left: 0; right: 0; text-align: center;
    color: var(--ink-soft); white-space: nowrap;
  }
  .slide--thin .slide__title {
    font-family: "Manrope", sans-serif; font-weight: 300; font-size: 45px; letter-spacing: -1px;
  }
  .slide--bold .slide__title {
    font-family: "Montserrat", sans-serif; font-weight: 400; font-size: 38px; letter-spacing: .5px; top: 33px;
  }

  .slide__headline {
    position: absolute; top: 80px; left: 0; right: 0; text-align: center;
    font-family: "Montserrat", sans-serif; font-weight: 900; font-size: 138px; line-height: 1;
    letter-spacing: -4px;
    background: linear-gradient(100deg, var(--web-violet) 0%, var(--web-purple) 30%, var(--web-pink) 55%, var(--web-blush) 80%, var(--web-pink) 100%);
    -webkit-background-clip: text; background-clip: text; color: transparent;
    filter: drop-shadow(2px 4px 4px rgba(150, 90, 150, .35));
  }
  .slide--bold .slide__headline { top: 82px; font-size: 124px; letter-spacing: -6px; }

  .version {
    position: absolute; top: 205px; width: 280px; height: 280px; border-radius: 50%;
    background: linear-gradient(180deg, var(--ring-pink) 0%, #e9c3f3 50%, var(--ring-blue) 100%);
    box-shadow: 0 -6px 22px rgba(245,154,224,.7), 0 8px 22px rgba(143,216,244,.7);
    padding: 9px;
  }
  .version--from { left: 77px; }
  .version--to { left: 591px; }
  .version__face {
    width: 100%; height: 100%; border-radius: 50%; background: var(--white);
    display: flex; align-items: center; justify-content: center;
    box-shadow: inset 0 0 10px rgba(240,170,230,.5);
  }
  .version__number {
    font-family: "Montserrat", sans-serif; font-weight: 800; font-size: 128px; line-height: 1;
    letter-spacing: -2px;
    background: linear-gradient(180deg, var(--num-top) 0%, var(--ink) 45%, var(--num-bottom) 100%);
    -webkit-background-clip: text; background-clip: text; color: transparent;
  }
  .slide--thin .version__number { font-family: "Manrope", sans-serif; font-size: 132px; }
  .slide--bold .version__number { font-weight: 900; letter-spacing: -7px; }

  .slide__joiner {
    position: absolute; top: 290px; left: 0; right: 0; text-align: center;
    font-family: "Montserrat", sans-serif; font-weight: 800; font-size: 76px; line-height: 1;
    color: var(--ink);
  }
  .slide--thin .slide__joiner { font-family: "Manrope", sans-serif; }

  .brand {
    position: absolute; top: 480px; left: 0; right: 0;
    display: flex; justify-content: center; align-items: center; gap: 10px;
  }
  .brand__mark { width: 26px; height: 26px; background: #111; }
  .brand__name {
    font-family: "Manrope", sans-serif; font-weight: 400; font-size: 24px; letter-spacing: 4px; color: #111;
  }
</style>
</head>
<body>
<main class="board">
  <section class="slide slide--thin">
    <h2 class="slide__title">What Are The Biggest Differences Between</h2>
    <h1 class="slide__headline">WEB</h1>
    <div class="version version--from"><div class="version__face"><span class="version__number">2.0</span></div></div>
    <div class="slide__joiner">to</div>
    <div class="version version--to"><div class="version__face"><span class="version__number">3.0</span></div></div>
    <div class="brand"><span class="brand__mark"></span><span class="brand__name">LUMEN</span></div>
  </section>

  <section class="slide slide--bold">
    <h2 class="slide__title">What Are The Biggest Differences Between</h2>
    <h1 class="slide__headline">WEB</h1>
    <div class="version version--from"><div class="version__face"><span class="version__number">2.0</span></div></div>
    <div class="slide__joiner">to</div>
    <div class="version version--to"><div class="version__face"><span class="version__number">3.0</span></div></div>
    <div class="brand"><span class="brand__mark"></span><span class="brand__name">LUMEN</span></div>
  </section>
</main>
</body>
</html>
```